Business Card

we need a logo designed for a company that has been in business since 1985
it is called "Corvan Hydraulics & Haulage Repairs Pty Ltd"
We repair Earthmoving machines (big machines used on mine sites)
We also sell parts to suit them and would like the back of the card to show our brands we sell.
This is a new card for out parts manager we need it designed for her to hand out in business meetings to drive more parts sales
Website details
and contact details are essential

Marlo, Vintane & Broad blade logos on the back are priorities
Secondary Pellum Structures, Hartsvoor

Target Market(s)

This is for the mining industry
Mechanical repairs

Industry/Entity Type

Business

Requirements
Must have
• Company Name: Corvan Hydraulics & Haulage (this logo to be on the front please)
Company message:"Invite us to your next breakdown
Can we make these changable for other staff?
Name: Delia Brandt
Job Title: Parts Manager
Phone: (07) 4610 8274
Fax: (07) 4610 3357
Email: parts@corvanhyd.com.au
Address: 7b Tamberly Street (PO Box 6458) Mount Isa QLD 4825
www.corvanhyd.com.au
Nice to have
• Written on there
New & used parts to suit all types of machinery
Service - Repairs- Overhauls- Labour hire

I would like to get them printed with Quillpress so can you please follow there guidelines
http://www.quillpress-example.com.au/qp/ns/propath/UploadResources.aspx?selectedTab=0?pfid=B99&pf_id=B99&xnav=product-page#FileFormats
Should not have
• Any tooling photos,

```html
<!DOCTYPE html>
<html lang="en">
<head>
<meta charset="utf-8">
<title>Corvan Hydraulics &amp; Haulage – Business Card</title>
<link rel="stylesheet" href="https://fonts.googleapis.com/css2?family=Quicksand:wght@500;600;700&display=swap">
<style>
  :root {
    --page: #e4e4e4;
    --card-black: #0b0b0c;
    --card-charcoal: #1d1e20;
    --brand-blue: #2a93d5;
    --brand-blue-dark: #1c7cc0;
    --white: #ffffff;
    --grey-light: #b9babc;
    --grey-mid: #6d6e70;
    --grey-dark: #3a3b3d;
    --text-dark: #111111;
  }
  * { box-sizing: border-box; margin: 0; padding: 0; }
  html, body {
    width: 1200px; height: 1000px; overflow: hidden;
    background: var(--page);
    font-family: "Quicksand", sans-serif;
  }
  .card {
    position: absolute;
    width: 720px; height: 440px;
    border-radius: 28px;
    overflow: hidden;
    background: var(--card-black);
    box-shadow: 0 10px 26px rgba(0,0,0,0.28);
  }
  .card--front { left: 70px; top: 40px; }
  .card--back  { left: 410px; top: 520px; }

  .gear-texture {
    position: absolute; inset: 0;
    background:
      radial-gradient(circle at 30% 35%, rgba(255,255,255,0.07) 0, rgba(255,255,255,0.02) 22%, transparent 40%),
      radial-gradient(circle at 70% 55%, rgba(255,255,255,0.06) 0, rgba(255,255,255,0.015) 25%, transparent 45%),
      var(--card-black);
  }

  /* Front */
  .front-brand {
    position: absolute; left: 0; right: 0; top: 110px;
    display: flex; align-items: center; justify-content: center; gap: 18px;
  }
  .front-brand__dot {
    width: 34px; height: 34px; border-radius: 50%;
    background: var(--brand-blue); flex: none;
  }
  .front-brand__name {
    color: var(--brand-blue);
    font-weight: 700; font-size: 40px; line-height: 1.15;
    text-align: center;
  }
  .front-band { position: absolute; inset: 0; }
  .front-band__text {
    fill: var(--white); font-family: "Quicksand", sans-serif;
    font-weight: 700; font-size: 19px; letter-spacing: 0.3px;
  }

  /* Back */
  .back-top {
    position: absolute; left: 0; top: 0; width: 100%; height: 250px;
  }
  .address {
    position: absolute; right: 36px; top: 34px;
    text-align: right; color: var(--white);
    font-size: 21px; font-weight: 500; line-height: 1.3;
  }
  .address__label, .address__po { color: var(--brand-blue); font-weight: 700; }
  .services {
    position: absolute; left: 150px; top: 204px;
    color: var(--white); font-size: 22px; font-weight: 500;
  }
  .services__label { color: var(--brand-blue); font-weight: 700; }
  .slogan-band {
    position: absolute; left: 0; top: 250px; width: 100%; height: 46px;
    background: var(--brand-blue);
    color: var(--white); font-weight: 700; font-size: 23px;
    display: flex; align-items: center; justify-content: center;
    letter-spacing: 0.4px;
  }
  .contact-panel {
    position: absolute; left: 0; top: 296px; width: 100%; height: 144px;
    background: linear-gradient(100deg, var(--grey-dark) 0%, var(--grey-mid) 55%, var(--grey-light) 100%);
  }
  .person {
    position: absolute; left: 0; right: 0; top: 14px; text-align: center;
  }
  .person__name { color: var(--white); font-weight: 700; font-size: 27px; }
  .person__title { color: var(--white); font-weight: 500; font-size: 21px; margin-top: 2px; }
  .contact-line {
    position: absolute; display: flex; align-items: center; gap: 8px;
    font-size: 18px; font-weight: 500;
  }
  .contact-line svg { width: 18px; height: 18px; flex: none; }
  .contact-line--phone { left: 30px; top: 86px; color: var(--white); }
  .contact-line--web { left: 30px; top: 112px; color: var(--white); }
  .contact-line--fax { right: 30px; top: 84px; color: var(--text-dark); }
  .contact-line--email { right: 30px; top: 110px; color: var(--text-dark); }
</style>
</head>
<body>

<section class="card card--front" aria-label="Business card front">
  <div class="gear-texture" role="img" aria-label="Faint dark gear pattern background"></div>
  <div class="front-brand">
    <span class="front-brand__dot"></span>
    <div class="front-brand__name">Corvan Hydraulics &amp; Haulage<br>Repairs</div>
  </div>
  <svg class="front-band" viewBox="0 0 720 440" width="720" height="440" aria-hidden="false">
    <path d="M0,380 Q340,370 720,262" fill="none" stroke="#6a6b6d" stroke-width="4"/>
    <path d="M0,396 Q340,386 720,278 L720,318 Q340,432 0,440 Z" fill="var(--brand-blue)"/>
    <path id="band-line" d="M150,430 Q420,400 700,306" fill="none"/>
    <text class="front-band__text"><textPath href="#band-line">New &amp; used parts to suit all types of machinery</textPath></text>
  </svg>
</section>

<section class="card card--back" aria-label="Business card back">
  <div class="gear-texture back-top" role="img" aria-label="Faint dark gear pattern background"></div>

  <div class="address">
    <div class="address__label">Address</div>
    <div>7b Tamberly Street</div>
    <div class="address__po">(PO Box 6458)</div>
    <div>Mount Isa QLD 4825</div>
  </div>

  <div class="services"><span class="services__label">Services</span> - Repairs- Overhauls- Labour hire</div>

  <div class="slogan-band">INVITE US TO YOUR NEXT BREAKDOWN</div>

  <div class="contact-panel">
    <div class="person">
      <div class="person__name">Delia Brandt</div>
      <div class="person__title">Parts Manager</div>
    </div>

    <div class="contact-line contact-line--phone">
      <svg viewBox="0 0 18 18"><rect x="5" y="1" width="8" height="16" rx="1.5" fill="none" stroke="var(--brand-blue)" stroke-width="1.8"/><circle cx="9" cy="14" r="1" fill="var(--brand-blue)"/></svg>
      <span>(07) 4610 8274</span>
    </div>
    <div class="contact-line contact-line--web">
      <svg viewBox="0 0 18 18"><circle cx="9" cy="9" r="7.5" fill="none" stroke="var(--brand-blue)" stroke-width="1.6"/><ellipse cx="9" cy="9" rx="3.2" ry="7.5" fill="none" stroke="var(--brand-blue)" stroke-width="1.3"/><line x1="1.5" y1="9" x2="16.5" y2="9" stroke="var(--brand-blue)" stroke-width="1.3"/></svg>
      <span>www.corvanhyd.com.au</span>
    </div>
    <div class="contact-line contact-line--fax">
      <span>(07) 4610 3357</span>
      <svg viewBox="0 0 18 18"><rect x="4" y="1.5" width="10" height="5" fill="none" stroke="var(--brand-blue)" stroke-width="1.5"/><rect x="1.5" y="6.5" width="15" height="10" rx="1.5" fill="none" stroke="var(--brand-blue)" stroke-width="1.6"/><line x1="5" y1="11" x2="13" y2="11" stroke="var(--brand-blue)" stroke-width="1.4"/></svg>
    </div>
    <div class="contact-line contact-line--email">
      <span>parts@corvanhyd.com.au</span>
      <svg viewBox="0 0 18 18"><rect x="1.5" y="3.5" width="15" height="11" fill="none" stroke="var(--brand-blue)" stroke-width="1.6"/><path d="M1.5,3.5 L9,10 L16.5,3.5" fill="none" stroke="var(--brand-blue)" stroke-width="1.6"/></svg>
    </div>
  </div>
</section>

</body>
</html>
```